Top Producing Realtor Business Card Design

Looking for branding with my logo on all of my materials. I am a top producing real estate agent, selling expensive homes in California. I'm looking for a classy design that includes my existing logo, the company corporate logo and my photo.

Looking forward to your submissions! Thank you so much! :)

I appreciate your submissions very much!  Excellent work!  I have revised the brief to be more clear about what I think I'm looking for.  Keep the submissions coming in!!  Thank you so much :)

Target Market(s)

Wealthy home buyers and sellers in California.

Industry/Entity Type

Real Estate

Requirements
Must have
• Must include:

Homestead Pinnacle Logo

Below Homestead Pinnacle Logo it must say: Alder Ridge (Helvetica font)

Complete address: 58317 Barwick Street
Alder Ridge, CA 94687

Phone number: 415.962.3057 cell
415.740.2195 VM 5821 office

My photo

My name: Mara Quinlow (please make sure it's correct before you submit) :)

My MQ Logo (if possible please keep logo colors the same)

"Realtor" with a reserved symbol after or below my name

My license number: StaREB #07428915

My website: www.MaraQuinlow-example.com

My email: Mara@MaraQuinlow-example.com

Nice to have
• I'm open minded :) The main goal is to have the MQ logo is on all of my material. For the business cards I sort of imagine my MQ logo in the background, and I like a fade. I prefer the logo to be on the front of the card, and I like it on the back of the card too, So a two sided business card is ok.

I prefer the light blue Homestead Pinnacle Logo submitted. Please note the light blue color must closely match :)

Another idea is the business card can be in the format of the yard sign photo submitted (maybe changed into the light blue color), to possibly be a business card that looks like the yard sign. The yard sign layout must closely match the example submitted due to corporate guidelines.

Basically I'm looking for something that will tie everything together with my photo and logo so it's well branded in the clients mind. :)

Should not have
• Please keep the logo's exactly as they are, including color...no need to change.

If you choose to use the yard sign example provided for the business card, Please do not change the basic layout of the yard sign submitted, I have to follow the corporate standards.

```html
<!DOCTYPE html>
<html lang="en">
<head>
<meta charset="utf-8">
<title>Mara Quinlow – Business Card</title>
<link rel="stylesheet" href="https://fonts.googleapis.com/css2?family=Montserrat:wght@300;400;500;600;700&family=Arimo:wght@400;700&display=swap">
<style>
  :root {
    --brand-blue: #0a56a3;
    --brand-light: #d6e4f1;
    --paper: #ffffff;
    --page: #ffffff;
    --photo-dark: #3f3d3c;
    --photo-mid: #8a8784;
  }
  * { margin: 0; padding: 0; box-sizing: border-box; }
  html, body { width: 1200px; height: 899px; overflow: hidden; background: var(--page); }
  body { position: relative; font-family: "Montserrat", sans-serif; }

  .card {
    position: absolute; left: 250px; top: 188px; width: 710px; height: 401px;
    background: var(--paper); border: 1px solid #d0d0d0;
    box-shadow: 4px 5px 6px rgba(0,0,0,0.35);
  }
  .brand-panel {
    position: absolute; left: 0; top: 0; width: 294px; height: 100%;
    background: var(--brand-blue); color: var(--paper); text-align: center;
  }
  .monogram {
    position: absolute; left: 0; right: 0; top: 76px;
    font-weight: 700; font-size: 140px; line-height: 1; color: var(--brand-light);
    letter-spacing: 4px;
  }
  .agent-name {
    position: absolute; left: 0; right: 0; top: 304px;
    font-weight: 700; font-size: 34px; line-height: 1;
  }
  .agent-title {
    position: absolute; left: 0; right: 0; top: 347px;
    font-weight: 400; font-size: 27px; line-height: 1; letter-spacing: 1px;
  }

  .contact {
    position: absolute; right: 208px; top: 207px; width: 196px;
    text-align: right; color: var(--brand-blue);
  }
  .address { font-size: 12.5px; line-height: 18px; font-weight: 500; }
  .phones { margin-top: 20px; font-weight: 700; }
  .phone-row { display: flex; justify-content: flex-end; align-items: baseline; line-height: 20px; }
  .phone-label { font-family: "Arimo", sans-serif; font-weight: 400; font-size: 10px; margin-right: auto; }
  .phone-number { font-size: 18px; }
  .voicemail { font-size: 16px; line-height: 17px; }
  .voicemail small { font-family: "Arimo", sans-serif; font-weight: 400; font-size: 10px; }
  .web { margin-top: 10px; font-weight: 700; font-size: 10px; line-height: 14px; white-space: nowrap; }

  .office-panel {
    position: absolute; left: 516px; top: 27px; width: 165px; height: 345px;
    background: var(--brand-blue); color: var(--paper); text-align: center;
  }
  .company-name {
    position: absolute; left: 14px; right: 14px; top: 20px; height: 56px;
    display: flex; align-items: center; justify-content: center; gap: 6px;
    font-weight: 700; font-size: 14px; line-height: 17px;
  }
  .company-name .mark { width: 10px; height: 10px; background: var(--brand-light); flex: none; }
  .office-city {
    position: absolute; left: 0; right: 0; top: 85px;
    font-family: "Arimo", sans-serif; font-size: 15px;
  }
  .agent-photo {
    position: absolute; left: 10px; top: 125px; width: 145px; height: 182px;
    background: radial-gradient(circle at 50% 40%, var(--photo-mid), var(--photo-dark));
  }
  .license {
    position: absolute; left: 0; right: 0; top: 314px;
    font-family: "Arimo", sans-serif; font-weight: 700; font-size: 13px;
  }

  .back-band {
    position: absolute; left: 0; top: 717px; width: 1200px; height: 182px;
    background: var(--brand-blue); color: var(--paper);
    box-shadow: 0 -3px 5px rgba(0,0,0,0.25);
  }
  .back-monogram {
    position: absolute; left: 62px; top: 48px; width: 140px; text-align: center;
    font-weight: 700; font-size: 70px; line-height: 1; color: var(--brand-light);
  }
  .back-name {
    position: absolute; right: 57px; top: 70px; text-align: center;
  }
  .back-name .agent-line { font-weight: 700; font-size: 34px; line-height: 1; }
  .back-name .title-line { font-weight: 400; font-size: 26px; line-height: 1; margin-top: 5px; letter-spacing: 1px; }
</style>
</head>
<body>
  <section class="card">
    <div class="brand-panel">
      <div class="monogram">MQ</div>
      <div class="agent-name">Mara Quinlow</div>
      <div class="agent-title">AGENT</div>
    </div>

    <div class="contact">
      <p class="address">58317 Barwick Street,<br>Alder Ridge, CA 94687</p>
      <div class="phones">
        <div class="phone-row"><span class="phone-label">Cell</span><span class="phone-number">415.962.3057</span></div>
        <div class="phone-row"><span class="phone-label">Office</span><span class="phone-number">415.740.2195</span></div>
        <div class="voicemail"><small>VM</small> 5821</div>
      </div>
      <p class="web">Mara@MaraQuinlow-example.com<br>www.MaraQuinlow-example.com</p>
    </div>

    <div class="office-panel">
      <div class="company-name"><span class="mark"></span><span>Homestead Pinnacle</span></div>
      <div class="office-city">Alder Ridge</div>
      <div class="agent-photo" role="img" aria-label="Portrait photo of the agent"></div>
      <div class="license">StaREB #07428915</div>
    </div>
  </section>

  <section class="back-band">
    <div class="back-monogram">MQ</div>
    <div class="back-name">
      <div class="agent-line">Mara Quinlow</div>
      <div class="title-line">AGENT</div>
    </div>
  </section>
</body>
</html>
```